VoltNest EV Charger Installation

We are an electrical contractor "Brannock Electric" http://brannockelectricservices.example.

New site is for a division we are creating. http://voltnestelectric.example/ is registered on Google domains.
Company is registered as VoltNest LLC.
VoltNest is something we are trying out to see if we can find a niche installing EV chargers and EV Charger outlets in existing homes and businesses. Looking to work it as a division off from Brannock Electric short term and if successful it would become a stand alone business. Often times this requires additional work to meet code. Work such as adding smoke & carbon monoxide detectors, new electrical panels and upgrading the electrical Main Service Meter system.
Will need to coordinate this site with our current Brannock Electric website. Not sure how this can work. We like the look of our current Brannock Electric Wordpress site, but it is dated and broken, in need of a rebuild or repair as well.
Need a website as a landing point for Google Maps inquiries and possibly as a way to drive customers to call for our services. Need to be mindful that we want to avoid confusion with people looking for EV charger Stations to drive and plug in their cars. We are a contractor not a place to plug in! The name may be problematic in this sense.
Looking for a site that coordinates style & color with the provided VoltNest logo. Would like to have a contact / inquiry page with a captcha or similar tool to weed out spam. need to integrate google maps and similar tools to measure marketing, assist in lead generation, etc.
Have Logo artwork. Not sure what format is best to upload.

Target Market(s)

People with electric cars, business owners and homeowners.

Industry/Entity Type

Electrical Contractor- Residential & Light Commercial (mostly residential)

Coding

Coded - Design and coding required

Number of Pages Required

3 page

Requirements
Must have
• Landing Page/about us , Contact Us/ inquiry Page with a quality captcha filter, Job Gallery- we don't have many pics yet. Google pointers /tools. Open to suggestions here! Mobile Phone/ Tablet friendly is important. I listed coded design but not quite sure what that means.
Nice to have
• Similar to the Brannock Electric site style a possibility, but open to suggestions. Possibly have something that shows the business is connected to Brannock Electric? ..."A division of Brannock Electric" with logo/link to site?

```html
<!DOCTYPE html>
<html lang="en">
<head>
<meta charset="utf-8">
<title>VoltNest EV Charger Installation</title>
<link rel="stylesheet" href="https://fonts.googleapis.com/css2?family=Syncopate:wght@400;700&family=Raleway:wght@400;500;600;700&display=swap">
<style>
:root{
  --green:#7bc143;
  --green-dark:#5e9e2c;
  --green-pale:#e6f3dc;
  --brown:#3a2614;
  --brown-band:#4b3e1b;
  --ink:#2e1f10;
  --text:#3d3d3d;
  --white:#ffffff;
}
*{margin:0;padding:0;box-sizing:border-box}
html,body{width:1200px;height:4580px;overflow:hidden}
body{position:relative;font-family:"Raleway",sans-serif;color:var(--text);background:var(--white)}
.abs{position:absolute}
.heading{font-family:"Syncopate",sans-serif;font-weight:700;color:var(--ink);letter-spacing:1px;text-transform:uppercase}

/* header */
.site-header{top:0;left:0;width:1200px;height:80px;background:var(--white)}
.brand-block{top:0;left:0;width:370px;height:76px;background:var(--brown);clip-path:polygon(0 0,100% 0,92% 100%,0 100%)}
.brand-name{font-family:"Syncopate",sans-serif;font-weight:700;color:var(--white);font-size:19px;letter-spacing:1px;display:flex;align-items:center;gap:10px}
.brand-name .dot{width:14px;height:14px;background:var(--green)}
.site-header .brand-name{top:24px;left:100px}
.main-nav a{position:absolute;top:30px;font-size:16px;color:var(--ink);text-decoration:none;font-weight:500}
.phone-btn{top:25px;left:978px;width:170px;height:28px;background:var(--green);color:var(--white);font-size:15px;display:flex;align-items:center;gap:8px;padding-left:6px;border-radius:2px}
.phone-btn .ico{width:22px;height:22px;border-radius:50%;background:var(--white);display:flex;align-items:center;justify-content:center}

/* hero */
.hero{top:80px;left:0;width:1200px;height:681px;background:linear-gradient(115deg,#dfeccd 0%,#b9d98e 22%,#e9f1e1 45%,#f3f5f1 62%,#c9d3c2 80%,#7a8a6e 100%)}
.hero-title{left:107px;top:238px;font-size:58px;line-height:78px}
.hero-title .accent{color:var(--green)}
.hero-arrow{top:321px;width:24px;height:24px;border:2px solid var(--ink);border-radius:50%;display:flex;align-items:center;justify-content:center}

/* about */
.about-title{top:848px;left:0;width:782px;text-align:center;font-size:38px}
.about-copy{top:916px;left:128px;width:555px;font-size:17px;line-height:29px}
.about-copy p{margin-bottom:29px}
.about-shape{top:871px;left:754px;width:350px;height:393px}
.btn{display:flex;align-items:center;justify-content:center;background:var(--white);border:1px solid #c7c7c7;box-shadow:2px 3px 4px rgba(0,0,0,.25);color:var(--green-dark);font-weight:700;font-size:14px;letter-spacing:.5px;text-transform:uppercase}
.btn-bolt{position:absolute;right:-12px;top:-6px}

/* services */
.services{top:1404px;left:0;width:1200px;height:632px;background:var(--green-pale)}
.services-title{top:1497px;left:0;width:1200px;text-align:center;font-size:38px}
.service-card{top:1600px;height:365px;background:var(--green);border-radius:34px;padding:18px 14px 0}
.service-card .photo{height:210px;border-radius:30px}
.service-card p{color:#2c2c1a;text-align:center;font-size:16px;line-height:25px;margin-top:18px}

/* division */
.division-title{top:2132px;left:0;width:1200px;text-align:center;font-size:38px}
.division-mark{top:2214px;left:0;width:1200px;text-align:center;font-family:"Syncopate",sans-serif;font-weight:700;font-size:22px;color:#b81f24;letter-spacing:1px}
.division-copy{top:2283px;left:130px;width:940px;text-align:center;font-size:17px;line-height:34px}

/* appointment */
.appointment{top:2626px;left:0;width:1200px;height:818px;background:linear-gradient(90deg,#6a5a48 0%,#847261 35%,#7a6957 65%,#5e4e3d 100%)}
.appointment-title{top:2700px;left:0;width:1182px;text-align:center;font-size:38px;color:var(--white)}
.form-card{top:2802px;left:229px;width:724px;height:427px;background:var(--white)}
.field{background:var(--green);color:var(--white);font-size:15px;padding:10px 22px;height:39px}
.field.select{display:flex;justify-content:space-between;align-items:center}

/* gallery */
.gallery-band{top:3444px;left:0;width:1200px;height:290px;background:var(--brown-band)}
.gallery-band-photo{top:3444px;left:0;width:125px;height:290px;background:linear-gradient(180deg,#5c6b3e,#7a4a2e)}
.gallery-title{top:3495px;left:560px;width:420px;text-align:center;font-size:38px;color:var(--white)}
.tile{border:4px solid var(--white);box-shadow:0 3px 8px rgba(0,0,0,.3)}

/* footer */
.site-footer{top:4166px;left:0;width:1200px;height:114px;background:var(--brown)}
.site-footer .brand-name{top:4212px;left:103px;font-size:22px}
.footer-nav a{position:absolute;top:4220px;color:var(--white);font-size:16px;text-decoration:none;font-weight:500}
.map{top:4280px;left:50px;width:1150px;height:197px;background:linear-gradient(135deg,#eceae3,#e2e5dc 50%,#dde3e8)}
.map-edge{top:4280px;left:0;width:50px;height:197px;background:#e6e3dc}
.bottom-bar{top:4477px;left:0;width:1200px;height:103px;background:var(--brown)}
.social{top:4511px;left:572px;display:flex;gap:6px}
.social span{width:16px;height:16px;background:var(--white);border-radius:3px}
.copyright{top:4551px;left:0;width:1200px;text-align:center;color:var(--white);font-size:13px}
</style>
</head>
<body>

<header class="site-header abs">
  <div class="brand-block abs"></div>
  <div class="brand-name abs"><span class="dot"></span>VOLTNEST</div>
  <svg class="abs" style="top:0;left:340px" width="40" height="76" viewBox="0 0 40 76"><polygon points="26,0 14,36 24,36 6,76 36,26 24,26 38,0" fill="#7bc143"/></svg>
  <nav class="main-nav">
    <a style="left:535px">Home</a>
    <a style="left:633px">About Us</a>
    <a style="left:745px">Gallery</a>
    <a style="left:843px">Contacts Us</a>
  </nav>
  <div class="phone-btn abs"><span class="ico"><svg width="12" height="12" viewBox="0 0 24 24"><path d="M6.6 10.8a15 15 0 0 0 6.6 6.6l2.2-2.2c.3-.3.7-.4 1-.2 1.1.4 2.3.6 3.6.6.6 0 1 .4 1 1V20c0 .6-.4 1-1 1A17 17 0 0 1 3 4c0-.6.4-1 1-1h3.5c.6 0 1 .4 1 1 0 1.3.2 2.5.6 3.6.1.3 0 .7-.2 1z" fill="#7bc143"/></svg></span>+1 555 010 0142</div>
</header>

<section class="hero abs" role="img" aria-label="Electric car plugged into a wall-mounted charger with glowing green light streaks"></section>
<h1 class="hero-title heading abs">Welcome to<br><span class="accent">VoltNest</span></h1>
<div class="hero-arrow abs" style="left:59px"><svg width="10" height="10" viewBox="0 0 10 10"><path d="M7 1 3 5l4 4" stroke="#2e1f10" stroke-width="1.6" fill="none"/></svg></div>
<div class="hero-arrow abs" style="left:1119px"><svg width="10" height="10" viewBox="0 0 10 10"><path d="M3 1l4 4-4 4" stroke="#2e1f10" stroke-width="1.6" fill="none"/></svg></div>

<h2 class="about-title heading abs">About Us</h2>
<div class="about-copy abs">
  <p>Electric vehicles (EVs) are here. Let VoltNest help you get powered up!</p>
  <p>EV charger installation is a relatively simple process, but it's important to hire a qualified electrician. VoltNest is a division of Brannock Electric, a licensed and insured electrical contractor. We are committed to providing our customers with a quality, code approved installation.</p>
  <p>We'll assess your home's electrical system and help find a safe and convenient location for the charger or charger outlet.</p>
</div>
<svg class="about-shape abs" viewBox="0 0 350 393">
  <polygon points="232,0 350,0 350,393 60,393 130,280 100,280 190,150 160,150" fill="#c7e5a8"/>
</svg>
<div class="abs" role="img" aria-label="Wall-mounted home EV charger with coiled cable on wood siding" style="top:885px;left:754px;width:348px;height:379px;background:linear-gradient(160deg,#e5ddd0,#b9ada0 60%,#6a635c);clip-path:polygon(75% 0,100% 0,100% 100%,0 100%)"></div>
<div class="btn abs" style="top:1287px;left:245px;width:274px;height:48px">Contact VoltNest Today
  <svg class="btn-bolt" width="20" height="56" viewBox="0 0 20 56"><polygon points="12,0 4,28 11,28 2,56 18,20 11,20 16,0" fill="#2e1f10"/></svg></div>

<section class="services abs"></section>
<h2 class="services-title heading abs">Our Services</h2>
<div class="service-card abs" style="left:87px;width:228px"><div class="photo" role="img" aria-label="Green wall-mounted EV charger" style="background:linear-gradient(160deg,#c9ccd0,#8d939a)"></div><p>installing EV chargers outlets in existing homes and businesses</p></div>
<div class="service-card abs" style="left:348px;width:226px"><div class="photo" role="img" aria-label="Ceiling smoke detector with green smoke" style="background:linear-gradient(160deg,#d9e6d2,#4fa04a)"></div><p>Adding smoke &amp; carbon monoxide detectors</p></div>
<div class="service-card abs" style="left:615px;width:226px"><div class="photo" role="img" aria-label="Rows of solar and electrical panels" style="background:linear-gradient(160deg,#c6b7d6,#2f6d4a 55%,#1f4a33)"></div><p>installing new electrical panels</p></div>
<div class="service-card abs" style="left:875px;width:225px"><div class="photo" role="img" aria-label="Gloved hands wiring a main service panel" style="background:linear-gradient(160deg,#dcd2ae,#8b8d45 55%,#3a3b22)"></div><p>upgrading the electrical Main Service Meter system</p></div>

<h2 class="division-title heading abs">A Division of Brannock Electric</h2>
<div class="division-mark abs">BRANNOCK ELECTRIC</div>
<div class="division-copy abs">Brannock Electric provides a full range of electrical services, installations, upgrades and repairs for homeowners, contractors, and businesses.<br>We understand that our customers are looking for the best ideas and value and we have the training and experience to provide sound, informative advice without gimmicks or high-pressure sales tactics. We pride ourselves in on-time service, take care in our work and guarantee a quality job, at a fair price.</div>
<div class="btn abs" style="top:2496px;left:516px;width:143px;height:48px">Read More
  <svg class="btn-bolt" width="20" height="56" viewBox="0 0 20 56"><polygon points="12,0 4,28 11,28 2,56 18,20 11,20 16,0" fill="#2e1f10"/></svg></div>

<section class="appointment abs" role="img" aria-label="Basement wall with battery units and electrical panels"></section>
<h2 class="appointment-title heading abs">Make an Appointment</h2>
<div class="form-card abs"></div>
<div class="field abs" style="top:2855px;left:284px;width:292px">First Name</div>
<div class="field abs" style="top:2855px;left:601px;width:291px">Last Name</div>
<div class="field abs" style="top:2946px;left:284px;width:292px">E-Mail</div>
<div class="field select abs" style="top:2946px;left:601px;width:293px">Type Of Service<svg width="14" height="8" viewBox="0 0 14 8"><path d="M1 1l6 6 6-6" stroke="#fff" stroke-width="1.5" fill="none"/></svg></div>
<div class="field abs" style="top:3037px;left:284px;width:608px;height:128px">Type here</div>
<div class="btn abs" style="top:3286px;left:466px;width:270px;height:46px">Make an Appointment
  <svg class="btn-bolt" width="20" height="56" viewBox="0 0 20 56"><polygon points="12,0 4,28 11,28 2,56 18,20 11,20 16,0" fill="#2e1f10"/></svg></div>

<section class="gallery-band abs"></section>
<div class="gallery-band-photo abs" role="img" aria-label="Outdoor electric meter on a house wall"></div>
<h2 class="gallery-title heading abs">Our Gallery</h2>
<div class="tile abs" role="img" aria-label="Open breaker panel with new wiring" style="top:3608px;left:137px;width:284px;height:211px;background:linear-gradient(160deg,#ecebe8,#b8b4ad)"></div>
<div class="tile abs" role="img" aria-label="Electric car parked beside a garage wall charger" style="top:3608px;left:457px;width:286px;height:215px;background:linear-gradient(160deg,#e9e7dc,#a7aaa6)"></div>
<div class="tile abs" role="img" aria-label="Close view of a labeled electrical panel" style="top:3608px;left:784px;width:286px;height:460px;background:linear-gradient(180deg,#eeeeec,#c9c9c6)"></div>
<div class="tile abs" role="img" aria-label="Row of battery and panel units on a basement wall" style="top:3858px;left:137px;width:606px;height:210px;background:linear-gradient(180deg,#8f8a82,#d8d4cd 60%,#6c665f)"></div>

<footer class="site-footer abs"></footer>
<div class="brand-name abs" style="top:4212px;left:103px;font-size:22px"><span class="dot"></span>VOLTNEST</div>
<nav class="footer-nav">
  <a style="left:663px">Home</a>
  <a style="left:765px">About Us</a>
  <a style="left:877px">Gallery</a>
  <a style="left:974px">Contacts Us</a>
</nav>
<div class="map-edge abs"></div>
<div class="map abs" role="img" aria-label="Street map showing the service area"></div>
<div class="bottom-bar abs"></div>
<div class="social abs"><span></span><span></span><span></span></div>
<div class="copyright abs">Copyright © 2023 VoltNest. All rights reserved.</div>

</body>
</html>
```